Polystyrene Recycling Material Flow

We need a diagram styled as an infographic that shows how polystyrene foam is recycled starting with a manufactured product, moving through the distribution process, waste material collection and reincorporation back into manufacturing. This is accomplished in different ways once the material is collected which needs to be clearly evident. The most important thing is for it to be simple enough to understand while still having a stylish look. The design can be with or without vector images or photography to depict the different stages. We are providing a very rudimentary 'sketch' of the information points and movement flow. Please see www.foamtradeunion.org (resources) to view our literature branding. The RGB & CMYK are attached.

Target Market(s)

Government Agencies, Brand Owners, Retailers, Recycling Industry

Industry/Entity Type

Packaging, Recycling, Manufacturing

Font styles to use
Sans Serif

Requirements
Must have
• Easy to Understand
Nice to have
• Images - either photography or vector illustrations - are optional. We have provided examples of both to show what could be used but are not required. Substituting your own interpretation of imagery is encouraged.
Should not have
• Outdated look.

```html
<!DOCTYPE html>
<html lang="en">
<head>
<meta charset="utf-8">
<title>Polystyrene Recycling Material Flow</title>
<link href="https://fonts.googleapis.com/css2?family=Roboto:wght@400;500;700&display=swap" rel="stylesheet">
<style>
:root{
  --flow:#f5a01c;
  --brown:#6a2d1b;
  --navy:#25323b;
  --olive:#9ba51b;
  --olive-line:#a9b53c;
  --gold:#b98f0e;
  --steel:#5b87a3;
  --band:#efe6e6;
  --ink:#1e1e1e;
  --muted:#555;
  --paper:#ffffff;
}
*{margin:0;padding:0;box-sizing:border-box}
html,body{width:1200px;height:814px;overflow:hidden;background:var(--paper)}
body{font-family:"Roboto",Arial,sans-serif;color:var(--ink)}
.canvas{position:relative;width:1200px;height:814px}
.abs{position:absolute}
.band{left:57px;top:348px;width:1089px;height:107px;background:var(--band)}
.flow-lines{position:absolute;left:0;top:0}
.title-block{left:846px;top:81px;width:265px;height:101px;background:var(--flow);color:#fff;text-align:center;font-weight:700;line-height:.95;display:flex;flex-direction:column;justify-content:center;align-items:center;gap:1px}
.title-block .t1{font-size:28px;letter-spacing:.4px}
.title-block .t2{font-size:36px}
.title-block .t3{font-size:25px;font-weight:500}
.sources-tag{left:151px;top:122px;width:39px;height:188px;background:var(--navy);color:#fff;font-weight:700;font-size:13px;display:flex;align-items:center;justify-content:center}
.sources-tag span{transform:rotate(-90deg);white-space:nowrap;letter-spacing:.3px}
.source{left:195px;height:45px;background:var(--brown);color:#fff;font-weight:700;font-size:14px;display:flex;align-items:center;padding-left:10px;white-space:nowrap}
.source-notes{left:386px;width:131px;height:45px;border:1px solid var(--brown);border-left:none;background:#fff;font-size:12.5px;color:var(--muted);display:flex;flex-direction:column;justify-content:center;padding-left:6px;line-height:1.3;white-space:nowrap}
.collection{left:574px;top:154px;width:128px;height:128px;border-radius:50%;border:1.5px solid var(--flow);background:#fff;display:flex;align-items:center;justify-content:center}
.collection span{width:116px;height:116px;border-radius:50%;background:var(--gold);color:#fff;font-weight:500;font-size:16.5px;display:flex;align-items:center;justify-content:center;letter-spacing:.3px}
.stage{height:45px;color:#fff;font-weight:500;font-size:17.5px;display:flex;align-items:center;justify-content:center;letter-spacing:.3px}
.stage.compaction{left:267px;top:381px;width:192px;background:var(--olive)}
.stage.regrind{left:759px;top:379px;width:192px;background:var(--steel)}
.side-note{font-size:12.5px;color:var(--muted);line-height:1.3;white-space:nowrap}
.side-note b{color:var(--olive);font-weight:700}
.side-note.blue b{color:var(--steel)}
.compaction-note{left:100px;top:389px;width:162px;text-align:right}
.regrind-note{left:958px;top:397px}
.shred-note{left:917px;top:514px}
.step{background:#fff;border:1.5px solid var(--olive-line);font-weight:500;font-size:13.5px;line-height:1.3;display:flex;align-items:center}
.step.left{padding-left:33px}
.step.center{justify-content:center;text-align:center;padding-right:20px}
.step.blue{border-color:var(--steel);justify-content:center;text-align:center}
.thumb{border-radius:50%;border:1.5px solid var(--olive-line);background:#fff;padding:2px}
.thumb.blue{border-color:var(--steel)}
.thumb i{display:block;width:100%;height:100%;border-radius:50%}
.fill-white{background:radial-gradient(circle at 40% 40%,#ffffff,#d9d9d9)}
.fill-pellet{background:radial-gradient(circle at 40% 40%,#f4f4f4,#bdbdbd)}
.fill-block{background:linear-gradient(135deg,#f7f7f7,#c9cdd2)}
.fill-work{background:linear-gradient(160deg,#d6e4ef,#7d98ae)}
.fill-comp{background:linear-gradient(160deg,#cfe0f0,#c9a77c)}
.pic{border-radius:4px}
</style>
</head>
<body>
<div class="canvas">
  <div class="abs band"></div>

  <svg class="flow-lines" width="1200" height="814" viewBox="0 0 1200 814" aria-hidden="true">
    <g fill="none" stroke="var(--flow)" stroke-width="2.5" stroke-dasharray="0.1 5" stroke-linecap="round">
      <path d="M100 748 V82 H636 V155"/>
      <path d="M431 426 V748 H100"/>
      <path d="M488 167 V194 M488 266 V239 M450 218 H575"/>
      <path d="M638 282 V406 M525 406 H704"/>
      <path d="M293 426 V488 M293 550 V577 M293 639 V662 M431 550 V577"/>
      <path d="M839 424 V508 M839 552 V578 M839 644 V744 H1110 V218 H702"/>
    </g>
    <g fill="var(--flow)">
      <polygon points="373,76 385,82 373,88"/>
      <polygon points="630,116 642,116 636,127"/>
      <polygon points="94,295 106,295 100,284"/>
      <polygon points="94,573 106,573 100,562"/>
      <polygon points="248,742 248,754 237,748"/>
      <polygon points="482,186 494,186 488,197"/>
      <polygon points="482,246 494,246 488,235"/>
      <polygon points="531,212 531,224 543,218"/>
      <polygon points="630,312 642,312 636,323"/>
      <polygon points="579,400 579,412 567,406"/>
      <polygon points="669,400 669,412 681,406"/>
      <polygon points="287,466 299,466 293,477"/>
      <polygon points="425,466 437,466 431,477"/>
      <polygon points="287,559 299,559 293,570"/>
      <polygon points="425,559 437,559 431,570"/>
      <polygon points="287,644 299,644 293,655"/>
      <polygon points="425,687 437,687 431,698"/>
      <polygon points="833,467 845,467 839,478"/>
      <polygon points="833,559 845,559 839,570"/>
      <polygon points="833,689 845,689 839,700"/>
      <polygon points="967,738 967,750 978,744"/>
      <polygon points="1104,573 1116,573 1110,562"/>
      <polygon points="1104,296 1116,296 1110,285"/>
      <polygon points="942,212 942,224 931,218"/>
    </g>
  </svg>

  <div class="abs title-block">
    <div class="t1">POLYSTYRENE</div>
    <div class="t2">RECYCLING</div>
    <div class="t3">MATERIAL FLOW</div>
  </div>

  <div class="abs sources-tag"><span>EPS WASTE SOURCES</span></div>

  <div class="abs source" style="top:122px;width:191px">MUNICIPAL WASTE</div>
  <div class="abs source-notes" style="top:122px"><span>• Curbside Collection</span><span>• Drop Off Centers</span></div>
  <div class="abs pic fill-work" style="left:522px;top:115px;width:36px;height:52px" role="img" aria-label="Recycling bin for foam drop off"></div>

  <div class="abs source" style="top:194px;width:194px">MANUFACTURING WASTE</div>
  <div class="abs pic" style="left:392px;top:190px;width:58px;height:49px;background:linear-gradient(180deg,#e9c44a,#5b7f95)" role="img" aria-label="Factory illustration"></div>

  <div class="abs source" style="top:266px;width:191px">COMMERCIAL WASTE</div>
  <div class="abs source-notes" style="top:266px"><span>• Back Hauling</span><span>• Localized Delivery</span></div>
  <div class="abs pic" style="left:521px;top:262px;width:67px;height:50px;background:linear-gradient(180deg,#7ccf3a,#3f6e2a)" role="img" aria-label="Green waste collection truck"></div>

  <div class="abs collection"><span>COLLECTION</span></div>
  <div class="abs pic" style="left:707px;top:225px;width:54px;height:56px;background:linear-gradient(180deg,#caa06a,#7d8fa6)" role="img" aria-label="Foam collection kiosk"></div>

  <div class="abs side-note compaction-note">Extruded Ingot <b>•</b><br>Hydrolic Compression <b>•</b></div>
  <div class="abs stage compaction">COMPACTION</div>
  <div class="abs thumb" style="left:460px;top:372px;width:64px;height:64px"><i class="fill-comp" role="img" aria-label="Worker beside compacted foam bale"></i></div>

  <div class="abs pic" style="left:705px;top:383px;width:51px;height:38px;border-radius:50%;background:radial-gradient(circle,#ffffff,#c9ccd0)" role="img" aria-label="Dish of reground foam beads"></div>
  <div class="abs stage regrind">REGRIND</div>
  <div class="abs side-note blue regrind-note"><b>•</b> Molder Facilities</div>

  <div class="abs step left" style="left:150px;top:488px;width:174px;height:62px">Recycled Content<br>EPS RESIN</div>
  <div class="abs thumb" style="left:127px;top:496px;width:48px;height:48px"><i class="fill-white" role="img" aria-label="Recycled EPS resin powder"></i></div>

  <div class="abs step left" style="left:150px;top:577px;width:174px;height:62px">RE-PELLETIZED<br>with Blowing Agent</div>
  <div class="abs thumb" style="left:127px;top:583px;width:48px;height:48px"><i class="fill-pellet" role="img" aria-label="Re-pelletized beads"></i></div>

  <div class="abs step left" style="left:150px;top:662px;width:212px;height:60px">EXPANDED POLYSTYRENE<br>Packaging &amp; Building<br>Products ≤50%</div>
  <div class="abs thumb" style="left:126px;top:668px;width:48px;height:48px"><i class="fill-block" role="img" aria-label="Foam packaging blocks"></i></div>

  <div class="abs step center" style="left:368px;top:488px;width:174px;height:62px">EXTRUDED<br>Rigid S Pellet</div>
  <div class="abs thumb" style="left:518px;top:495px;width:48px;height:48px"><i class="fill-pellet" role="img" aria-label="Rigid polystyrene pellets"></i></div>

  <div class="abs step center" style="left:368px;top:577px;width:174px;height:62px">END MARKET<br>Applications</div>
  <div class="abs thumb" style="left:519px;top:583px;width:48px;height:48px"><i class="fill-block" role="img" aria-label="Molded consumer product"></i></div>
  <div class="abs thumb" style="left:571px;top:583px;width:48px;height:48px"><i class="fill-work" role="img" aria-label="Building materials"></i></div>

  <div class="abs pic" style="left:702px;top:515px;width:52px;height:30px;border-radius:50%;background:radial-gradient(ellipse,#eeeeee,#ffffff)" role="img" aria-label="Shredded foam beads"></div>
  <div class="abs step blue" style="left:757px;top:508px;width:153px;height:44px">SHREDDING</div>
  <div class="abs side-note blue shred-note"><b>•</b> Homogenization<br><b>•</b> Mixing for Consistency</div>

  <div class="abs step blue" style="left:757px;top:578px;width:153px;height:66px">Recycled Content<br>PACKAGING ≤15%</div>
  <div class="abs thumb blue" style="left:915px;top:577px;width:70px;height:70px"><i class="fill-work" role="img" aria-label="Packaging production line"></i></div>
</div>
</body>
</html>
```